Miriams Professional Resume

Pls upgrade to make look more effective and perhaps add α photo on it, both options with photo and without would be great. Thanks very much. I would also like the resume so I can edit as well if I need to down the track.

Target Market(s)

This is my professional resume to make it more effective to potential senior hiring managers,

Colors
f04a50

Requirements
Must have
• Professional look.

```html
<!DOCTYPE html>
<html lang="en">
<head>
<meta charset="utf-8">
<title>Miriam Falk – Resume</title>
<link rel="stylesheet" href="https://fonts.googleapis.com/css2?family=Montserrat:wght@400;500&family=Raleway:wght@600;700&display=swap">
<style>
  :root {
    --accent: #12a2e2;
    --panel: #262626;
    --band-top: #3f95dc;
    --band-bottom: #2a79c4;
    --ink: #111111;
    --muted-ink: #e6e6e6;
    --rule: #dedede;
    --rule-dark: #8a8a8a;
    --photo-a: #e9ecef;
    --photo-b: #c9cfd6;
  }
  * { margin: 0; padding: 0; box-sizing: border-box; }
  html, body { width: 927px; height: 1200px; overflow: hidden; background: #fff; }
  body { font-family: "Montserrat", sans-serif; color: var(--ink); }
  .resume { position: relative; width: 927px; height: 1200px; overflow: hidden; }

  /* Sidebar */
  .sidebar { position: absolute; left: 0; top: 0; width: 315px; height: 1200px; background: var(--panel); color: var(--muted-ink); }
  .portrait { position: absolute; left: 0; top: 0; width: 315px; height: 265px; background: linear-gradient(160deg, var(--photo-a), var(--photo-b)); }
  .name-band { position: absolute; left: 0; top: 265px; width: 315px; height: 82px; background: linear-gradient(180deg, var(--band-top), var(--band-bottom)); border-bottom: 2px solid #1a5e9e; text-align: center; color: #fff; }
  .name-band h1 { font-family: "Raleway", sans-serif; font-weight: 700; font-size: 29px; letter-spacing: -0.5px; margin-top: 14px; line-height: 32px; }
  .name-band p { font-family: "Raleway", sans-serif; font-weight: 700; font-size: 15px; margin-top: 4px; }

  .side-heading { position: absolute; font-family: "Raleway", sans-serif; font-weight: 700; font-size: 18px; color: var(--accent); }
  .side-rule { position: absolute; height: 3px; background: var(--rule-dark); }
  .side-rule::before { content: ""; position: absolute; left: 0; top: 0; width: 41px; height: 3px; background: #fff; }

  .contact-item { position: absolute; left: 102px; font-size: 14px; color: #fff; }
  .contact-item.link { text-decoration: underline; }
  .contact-icon { position: absolute; left: 54px; width: 28px; height: 28px; }

  .edu { position: absolute; left: 48px; width: 262px; font-size: 14px; line-height: 19.5px; color: #e9e9e9; }
  .edu h3 { font-family: "Raleway", sans-serif; font-weight: 700; font-size: 14.5px; color: #fff; text-decoration: underline; line-height: 21px; margin-bottom: 4px; }

  .lang { position: absolute; left: 48px; font-family: "Raleway", sans-serif; font-weight: 700; font-size: 15px; color: #fff; }
  .lang-bar { position: absolute; left: 126px; width: 133px; height: 11px; border: 1.5px solid #fff; border-radius: 2px; background: #111; }
  .lang-bar span { display: block; height: 100%; width: 88%; background: var(--accent); }

  /* Main column */
  .main-heading { position: absolute; font-family: "Raleway", sans-serif; font-weight: 700; font-size: 17.5px; color: var(--accent); }
  .main-rule { position: absolute; height: 2px; background: var(--rule); }
  .main-rule::before { content: ""; position: absolute; left: 0; top: -1px; width: 41px; height: 4px; background: #000; }

  .statement { position: absolute; left: 365px; top: 101px; width: 514px; font-size: 12.6px; line-height: 17.8px; text-align: justify; }

  .job-line { position: absolute; font-family: "Raleway", sans-serif; font-weight: 700; font-size: 16px; color: #000; }

  .bullets { position: absolute; list-style: none; }
  .bullets li { position: relative; }
  .bullets li::before { content: ""; position: absolute; left: -22px; width: 6px; height: 6px; border-radius: 50%; background: #000; }
  .duties { left: 365px; top: 411px; width: 542px; font-size: 16px; line-height: 22.4px; text-align: justify; }
  .duties li::before { top: 9px; }
  .duties li:last-child { text-align: left; }
  .skills { left: 367px; top: 866px; width: 560px; font-size: 15.5px; line-height: 19.5px; }
  .skills li { margin-bottom: 1px; }
  .skills li::before { top: 8px; left: -25px; }
  .awards { left: 369px; top: 1064px; width: 520px; font-size: 16px; line-height: 19.5px; }
  .awards li { margin-bottom: 6px; }
  .awards li::before { top: 8px; left: -27px; }
  .awards strong { font-family: "Raleway", sans-serif; font-weight: 700; display: block; }
</style>
</head>
<body>
<div class="resume">

  <aside class="sidebar">
    <div class="portrait" role="img" aria-label="Portrait photo of Miriam Falk"></div>
    <div class="name-band">
      <h1>MIRIAM FALK</h1>
      <p>Senior Manager</p>
    </div>

    <h2 class="side-heading" style="left:53px; top:399px;">CONTACT</h2>
    <div class="side-rule" style="left:53px; top:427px; width:235px;"></div>

    <svg class="contact-icon" style="top:442px;" viewBox="0 0 28 28" fill="none" stroke="#fff" stroke-width="1.6" stroke-linejoin="round">
      <path d="M6 4 L10 3 L13 9 L10.5 11 C12 15 14 17 18 19 L20 16.5 L26 19.5 L25 23.5 C18 25 4 14 6 4 Z"/>
    </svg>
    <span class="contact-item" style="top:441px;">+61 400 555 018</span>

    <svg class="contact-icon" style="top:484px;" viewBox="0 0 28 28" fill="none" stroke="#fff" stroke-width="1.6">
      <rect x="2" y="6" width="24" height="16"/>
      <path d="M2 6 L14 16 L26 6 M2 22 L11 13.5 M26 22 L17 13.5"/>
    </svg>
    <span class="contact-item link" style="top:472px;">Miriamf @mailbox.com</span>

    <svg class="contact-icon" style="top:532px; width:31px; height:31px; left:53px;" viewBox="0 0 31 31" fill="none" stroke="#fff" stroke-width="1.8">
      <circle cx="15.5" cy="15.5" r="13.5"/>
    </svg>
    <span class="contact-item link" style="top:527px;">miriam-falk-3b7c10082</span>

    <svg class="contact-icon" style="top:580px;" viewBox="0 0 28 28">
      <path d="M14 2 C8.5 2 5 6 5 10.5 C5 16 14 26 14 26 C14 26 23 16 23 10.5 C23 6 19.5 2 14 2 Z" fill="#fff"/>
      <circle cx="14" cy="10.5" r="3.3" fill="var(--panel)"/>
    </svg>
    <span class="contact-item" style="top:577px;">Brisbane QLD 4000</span>

    <h2 class="side-heading" style="left:55px; top:625px;">EDUCATION</h2>
    <div class="side-rule" style="left:53px; top:652px; width:235px;"></div>

    <div class="edu" style="top:666px;">
      <h3>2016-AgileWorks</h3>
      Brisbane, Queensland, Australia<br>
      Certificate in Agile Facilitation and Iteration Management
    </div>

    <div class="edu" style="top:786px;">
      <h3>2015-BRISCO Training Assessment and Education</h3>
      Brisbane, Queensland, Australia<br>
      Training and Assessment<br>
      Certificate IV TAE
    </div>

    <div class="edu" style="top:909px;">
      <h3>2008-Riverbend University</h3>
      Brisbane, Queensland, Australia<br>
      Human Resource Management<br>
      Bachelor Business
    </div>

    <h2 class="side-heading" style="left:48px; top:1020px;">Languages</h2>
    <div class="side-rule" style="left:45px; top:1050px; width:236px;"></div>

    <span class="lang" style="top:1069px;">English</span>
    <div class="lang-bar" style="top:1069px;"><span></span></div>
    <span class="lang" style="top:1099px;">Spanish</span>
    <div class="lang-bar" style="top:1099px;"><span></span></div>
  </aside>

  <main>
    <h2 class="main-heading" style="left:368px; top:48px;">Professional Statement:</h2>
    <div class="main-rule" style="left:368px; top:78px; width:493px;"></div>
    <p class="statement">My strength is in leadership, developing strategies and providing excellence in HR Operational Services, Recruiting, People Development and building high performing teams to accelerate business performance and drive engagement. Masters in Strategic Organisational Development. As an authentic leader I excel at navigating across the business to build a positive culture while consulting with executives to understand imperative business needs and recommend the best solution. Successfully rolled out Fizzwell Project for 200 + new customer sites for the ORCHA Fresh Fruit Project and actively recruited for 20 + technical field service agents, developed their capabilities and achieved 100 % completion of the project.</p>

    <h2 class="main-heading" style="left:367px; top:307px;">WORK EXPERIENCE</h2>
    <div class="main-rule" style="left:368px; top:335px; width:493px;"></div>

    <span class="job-line" style="left:356px; top:347px;">Service Delivery Advisor</span>
    <span class="job-line" style="left:627px; top:347px;">JANUARY 2018 - PRESENT</span>
    <span class="job-line" style="left:356px; top:381px;">Northbay Group</span>
    <span class="job-line" style="left:627px; top:381px;">BRISBANE</span>

    <ul class="bullets duties">
      <li>Design, maintain, adapt and govern Learning’s service delivery model to deliver the transformation of Learning product, service and delivery in line with Learning Optimisation targets.</li>
      <li>Ensure the efficient and effective flow of work through the Learning value chain and smooth collaboration between the internal and external Learning workforce</li>
      <li>Act as a conduit between the Capability team in Strategic Advice, Product Owners, Learning Experience, Advice &amp; Services, Partners and relevant stakeholders to ensure on time delivery to agreed costs.</li>
      <li>Thought Leader on emerging trends and drive the continuous improvement of Learning process and policy, including Staff Study framework</li>
      <li>Identify problems across the Learning value chain and contribute data sources to ensure visibility and effective resolution through the Learning Governance Forum.</li>
      <li>Design, track and and report on the status of performance and quality improvement efforts and impacts.</li>
    </ul>

    <h2 class="main-heading" style="left:366px; top:818px;">Skills</h2>
    <div class="main-rule" style="left:364px; top:846px; width:494px;"></div>

    <ul class="bullets skills">
      <li>Supports the quarterly/ annual planning and prioritisation</li>
      <li>Assists the PX Advisor with putting proposals together that will improve processes and client experience</li>
      <li>Provides input on future systems and process requirement</li>
      <li>Attends swarms and provides advice on Learning solution viability within the Learning Management System (Our Learning Space)</li>
      <li>Maintains and governs project status and raises risks as required.</li>
    </ul>

    <h2 class="main-heading" style="left:359px; top:1019px;">Awards</h2>
    <div class="main-rule" style="left:361px; top:1049px; width:494px;"></div>

    <ul class="bullets awards">
      <li><strong>2017</strong>Lightning round Speaker at Agile Summit - Learning Transformation</li>
      <li><strong>2017</strong>Quarterly HR Team Award - Streamlining Leadership Program</li>
    </ul>
  </main>

</div>
</body>
</html>
```